Real estate broker business card

Want a modern celan but effective business card for my residential and commercial real estate business. I want the back of the card to advertise my services and to capture business. I have attached the back of my current business card fore ideas
Updates

Target Market(s)

home buyers and seller. commercial buyers and sellers

Industry/Entity Type

Real Estate

Contact Information for Business Card

must have my contact information and my photo

Requirements
Must have
• Lorna Vettridge
• Owner & Qualifying Broker
• Brockhill Real Estate Services
• 555.218.7094
• lorna@brockhillhomes.example
• www.brockhillhomes.example
Nice to have
• metallic
• Business capture text: " Don't buy or lease property without someone looking out for your best interests. I will represent you on your home or investment purchase for FREE!"
• "Home owners, call today to receive a FREE market analysis for your homes value!

```html
<!DOCTYPE html>
<html lang="en">
<head>
<meta charset="utf-8">
<title>Brockhill Real Estate Services – Business Card</title>
<link rel="stylesheet" href="https://fonts.googleapis.com/css2?family=Cinzel:wght@500&family=Open+Sans:wght@300;400&display=swap">
<style>
  :root {
    --stage: #8a8b8c;
    --card: #ffffff;
    --teal: #1f95a2;
    --teal-deep: #146f7a;
    --ink: #4a4d50;
    --ink-soft: #6a6d70;
    --photo-dark: #2f3a2c;
    --photo-light: #c9c2bb;
  }
  * { box-sizing: border-box; margin: 0; padding: 0; }
  html, body { width: 1200px; height: 950px; overflow: hidden; }
  body {
    background: var(--stage);
    font-family: "Open Sans", Arial, sans-serif;
    color: var(--ink);
    position: relative;
  }
  .card {
    position: absolute;
    left: 232px;
    width: 736px;
    height: 420px;
    background: var(--card);
    box-shadow: 0 6px 18px rgba(0,0,0,.35);
    overflow: hidden;
  }
  .card--front { top: 40px; }
  .card--back  { top: 490px; }

  /* front */
  .brand {
    position: absolute;
    left: 0; right: 0; top: 120px;
    display: flex; align-items: center; justify-content: center; gap: 16px;
  }
  .brand__dot {
    width: 44px; height: 44px; border-radius: 50%;
    background: var(--teal);
  }
  .brand__name {
    font-family: "Cinzel", Georgia, serif;
    font-weight: 500;
    font-size: 30px;
    color: var(--teal);
    letter-spacing: 1px;
  }
  .front__offer {
    position: absolute;
    left: 0; right: 0; top: 265px;
    text-align: center;
    font-size: 19px;
    line-height: 1.4;
    color: var(--ink-soft);
  }

  /* back */
  .portrait {
    position: absolute;
    left: 40px; top: 46px;
    width: 180px; height: 150px;
    border-radius: 10px;
    background: radial-gradient(circle at 55% 55%, var(--photo-light) 0%, #8b7e74 45%, var(--photo-dark) 100%);
  }
  .agent {
    position: absolute;
    left: 40px; top: 214px;
  }
  .agent__name {
    font-family: "Cinzel", Georgia, serif;
    font-weight: 500;
    font-size: 27px;
    color: var(--teal);
    letter-spacing: .5px;
    line-height: 1.1;
  }
  .agent__role {
    font-size: 18px;
    font-weight: 300;
    line-height: 1.35;
    color: var(--ink);
    margin-top: 2px;
  }
  .contact {
    list-style: none;
    margin-top: 14px;
  }
  .contact__item {
    display: flex; align-items: center; gap: 10px;
    font-size: 17px;
    font-weight: 300;
    line-height: 1.55;
  }
  .contact__icon { width: 16px; height: 16px; flex: none; }

  .back-brand {
    position: absolute;
    right: 60px; top: 120px;
    display: flex; flex-direction: column; align-items: center; gap: 18px;
  }
  .back-brand__mark {
    width: 170px; height: 170px; border-radius: 50%;
    background: linear-gradient(160deg, var(--teal) 0%, var(--teal-deep) 100%);
  }
  .back-brand__name {
    font-family: "Cinzel", Georgia, serif;
    font-weight: 500;
    font-size: 26px;
    color: var(--teal);
    letter-spacing: 1px;
  }
</style>
</head>
<body>

  <section class="card card--front" aria-label="Card front">
    <div class="brand">
      <span class="brand__dot"></span>
      <span class="brand__name">Brockhill Real Estate Services</span>
    </div>
    <p class="front__offer">Home owners, call today to receive a FREE<br>market analysis for your homes value!</p>
  </section>

  <section class="card card--back" aria-label="Card back">
    <div class="portrait" role="img" aria-label="Portrait photo of Lorna Vettridge"></div>

    <div class="agent">
      <h1 class="agent__name">Lorna Vettridge</h1>
      <p class="agent__role">Owner &amp; Qualifying Broker<br>Brockhill Real Estate Services</p>

      <ul class="contact">
        <li class="contact__item">
          <svg class="contact__icon" viewBox="0 0 16 16" aria-hidden="true">
            <path fill="var(--ink)" d="M3.6 1.2l2.3 2.6-1.3 1.8c.9 2 2.3 3.5 4.4 4.6l1.6-1.3 2.6 2.2-1.4 2.2c-5.4-.6-9.8-5-10.3-10.4z"/>
          </svg>
          <span>555.218.7094</span>
        </li>
        <li class="contact__item">
          <svg class="contact__icon" viewBox="0 0 16 16" aria-hidden="true">
            <rect x="1" y="3" width="14" height="10" rx="1" fill="var(--ink)"/>
            <path d="M1.5 3.8L8 9l6.5-5.2" fill="none" stroke="#fff" stroke-width="1.2"/>
          </svg>
          <span>lorna@brockhillhomes.example</span>
        </li>
        <li class="contact__item">
          <svg class="contact__icon" viewBox="0 0 16 16" aria-hidden="true">
            <circle cx="8" cy="8" r="7" fill="var(--ink)"/>
            <path d="M1.5 8h13M8 1.2c-2.4 2-2.4 11.6 0 13.6M8 1.2c2.4 2 2.4 11.6 0 13.6" fill="none" stroke="#fff" stroke-width="1"/>
          </svg>
          <span>www.brockhillhomes.example</span>
        </li>
      </ul>
    </div>

    <div class="back-brand">
      <span class="back-brand__mark"></span>
      <span class="back-brand__name">Brockhill</span>
    </div>
  </section>

</body>
</html>
```